Orbin Vale Systems

Our company is about IT hardwares and IT solutions. IT hardware such as PC, RAMS, storage and servers. IT solutions such as project management, BA. We are also selling new technology too.

Target Market(s)

Consumer, Small to Medium Business, Corporate

Requirements
Must have
• The business card must have the following:
• Name:
• Title:
• Contact Number:
• Email address:
• Website:
• Color: Must match the logo color upgrade

```html
<!DOCTYPE html>
<html lang="en">
<head>
<meta charset="utf-8">
<title>Orbin Vale Systems – Business Card</title>
<link href="https://fonts.googleapis.com/css2?family=Lato:wght@400;700;900&display=swap" rel="stylesheet">
<style>
  :root {
    --bg: #3a3a3a;
    --orange: #c1692a;
    --charcoal: #474747;
    --ink: #2b2b2b;
    --white: #ffffff;
  }
  * { margin: 0; padding: 0; box-sizing: border-box; }
  html, body { width: 1200px; height: 782px; overflow: hidden; }
  body {
    background: var(--bg);
    font-family: 'Lato', sans-serif;
    position: relative;
  }
  .card {
    position: absolute;
    left: 340px;
    width: 520px;
    height: 298px;
    overflow: hidden;
    box-shadow: 0 6px 18px rgba(0,0,0,.35);
  }
  .card--front { top: 58px; background: var(--orange); color: var(--white); }
  .card--back  { top: 420px; background: var(--white); }

  /* front */
  .front-brand {
    position: absolute; left: 0; right: 0; top: 92px;
    text-align: center;
  }
  .front-brand .mark {
    width: 22px; height: 22px; border: 3px solid var(--white);
    margin: 0 auto 12px;
  }
  .brand-name {
    font-weight: 900; text-transform: uppercase; line-height: 1;
  }
  .front-brand .brand-name { font-size: 40px; letter-spacing: 1px; }
  .front-brand .brand-sub { font-size: 16px; letter-spacing: 11px; margin-top: 6px; padding-left: 11px; }
  .tagline {
    margin-top: 16px; font-weight: 400; font-size: 13px; letter-spacing: 1.5px;
  }

  /* back */
  .contact { position: absolute; left: 34px; top: 30px; color: var(--ink); }
  .person-name { color: var(--orange); font-size: 17px; font-weight: 400; letter-spacing: .5px; text-transform: uppercase; }
  .person-title { font-size: 12.5px; margin-top: 1px; }
  .contact-list { list-style: none; margin-top: 12px; font-size: 12.5px; }
  .contact-list li { display: flex; align-items: center; gap: 7px; line-height: 19px; }
  .contact-list svg { width: 10px; height: 10px; fill: var(--orange); flex: none; }

  .back-brand {
    position: absolute; right: 34px; top: 92px;
    display: flex; align-items: center; gap: 10px; color: var(--charcoal);
  }
  .back-brand .mark { width: 18px; height: 18px; background: var(--orange); }
  .back-brand .brand-name { font-size: 30px; }
  .back-brand .brand-sub { font-size: 12px; letter-spacing: 8px; margin-top: 4px; }

  .footer-rule {
    position: absolute; left: 0; right: 0; top: 214px; height: 6px;
    background: var(--orange);
  }
  .footer-band {
    position: absolute; left: 0; right: 0; top: 226px; bottom: 0;
    background: var(--charcoal);
  }
</style>
</head>
<body>
  <section class="card card--front">
    <div class="front-brand">
      <div class="mark"></div>
      <div class="brand-name">Orbin Vale</div>
      <div class="brand-name brand-sub">Systems</div>
      <p class="tagline">IT HARDWARES AND IT SOLUTIONS</p>
    </div>
  </section>

  <section class="card card--back">
    <div class="footer-rule"></div>
    <div class="footer-band"></div>

    <div class="contact">
      <h1 class="person-name">Marcus Hale</h1>
      <p class="person-title">Managing Director</p>
      <ul class="contact-list">
        <li><svg viewBox="0 0 10 10"><path d="M2 0 L4 2.5 L3 3.6 Q4.3 5.9 6.4 7 L7.5 6 L10 8 L8.5 10 Q2 9 0 1.5 Z"/></svg>044-987 654 321</li>
        <li><svg viewBox="0 0 10 10"><path d="M0 2 H10 V8 H0 Z M0 2 L5 6 L10 2" /></svg>info@orbinvale.com</li>
        <li><svg viewBox="0 0 10 10"><circle cx="5" cy="5" r="5"/></svg>www.orbinvale.com</li>
      </ul>
    </div>

    <div class="back-brand">
      <div class="mark"></div>
      <div>
        <div class="brand-name">Orbin Vale</div>
        <div class="brand-name brand-sub">Systems</div>
      </div>
    </div>
  </section>
</body>
</html>
```